Recruitment Site Design

We need a design for the login page, about page, and inner pages of a recruitment site for an oil and gas company. Design should be modern, sleek, professional and colors can be blue, green, white, orange or any other recommended colors.

Please also take into consideration that once the users login, they will need to access a form to fill in their information.

** UPDATE: Kindly provide a design for the inner information page consistent with the outer design. Attached is a picture of the basic structure. ***
Updates

Please provide a design for inner pages as shown in the design brief consistent with the registration page provided. 

Reason: We're extending it to get more inside pages.

Target Market(s)

Professionals looking for a career in the oil and gas industry in the Middle East.

Industry/Entity Type

Oil And Gas

Requirements
Must have
• Sleek design

```html
<!DOCTYPE html>
<html lang="en">
<head>
<meta charset="UTF-8">
<title>Recruitment site – Login</title>
<link rel="stylesheet" href="https://fonts.googleapis.com/css2?family=Open+Sans:wght@400;600&family=Gelasio&family=Arimo&display=swap">
<style>
:root{
  --header-top:#2a7ef8;
  --header-bottom:#62a3fb;
  --footer-top:#6ea8f9;
  --footer-bottom:#92c0fd;
  --white:#ffffff;
  --ink:#111111;
  --body-text:#4a4a4a;
  --muted:#666666;
  --link:#5d9ff0;
  --accent:#fcc800;
  --button-grey:#6f6f6f;
  --field-border:#b9b9b9;
  --scene-light:#c4c4c4;
  --scene-mid:#8a8a8a;
  --scene-dark:#4a4a4a;
}
*{box-sizing:border-box;margin:0;padding:0}
html,body{width:1200px;height:1200px;overflow:hidden}
body{position:relative;background:var(--scene-mid);font-family:"Arimo",Arial,sans-serif}

.site-header{position:absolute;left:0;top:0;width:1200px;height:113px;
  background:linear-gradient(var(--header-top),var(--header-bottom));
  box-shadow:0 2px 4px rgba(0,0,0,.35);z-index:2}
.brand{position:absolute;left:100px;top:36px;font-family:"Open Sans",sans-serif;font-weight:600;
  font-size:34px;color:var(--white);line-height:48px}
.main-nav{position:absolute;right:103px;top:61px;display:flex;font-family:"Open Sans",sans-serif;
  font-size:13px;color:var(--white)}
.main-nav span{padding:0 16px}
.main-nav span+span{border-left:1.5px solid var(--white)}
.main-nav span:last-child{padding-right:0}

.hero-backdrop{position:absolute;left:0;top:113px;width:1200px;height:1005px;
  background:linear-gradient(180deg,var(--scene-light) 0%,#b3b3b3 25%,var(--scene-mid) 60%,var(--scene-dark) 100%)}

.hero-intro{position:absolute;left:115px;top:312px;width:510px;font-family:"Gelasio",serif;
  font-size:30px;line-height:36px;letter-spacing:.3px;color:var(--ink)}

.login-card{position:absolute;left:650px;top:320px;width:415px;height:339px;background:var(--white);
  border-radius:8px;border:1px solid #ddd}
.field{position:absolute;left:24px;width:333px;height:33px;border:1px solid var(--field-border);
  border-top:2px solid #9a9a9a;font-size:14px;color:#8a8a8a;padding:7px 11px;letter-spacing:.3px}
.field.user{top:33px}
.field.pass{top:84px}
.btn{position:absolute;height:31px;width:113px;border-radius:4px;text-align:center;
  font-size:15px;line-height:31px;letter-spacing:.5px}
.btn.signin{left:239px;top:139px;background:var(--accent);color:var(--ink)}
.login-note{position:absolute;left:25px;font-size:14px;color:var(--muted)}
.login-note a{color:var(--link);text-decoration:underline}
.login-note.forgot{top:221px}
.login-note.register{top:272px}

.welcome-card{position:absolute;left:100px;top:744px;width:1001px;height:284px;background:var(--white);
  border-radius:8px}
.welcome-photo{position:absolute;left:31px;top:44px;width:261px;height:196px;
  background:linear-gradient(180deg,#5d8fd6 0%,#a8c2e6 40%,#a89a7e 65%,#c9c3b7 100%)}
.welcome-title{position:absolute;left:325px;top:40px;font-size:24px;font-weight:400;color:var(--accent);font-family:"Arimo",Arial,sans-serif}
.welcome-text{position:absolute;left:328px;top:75px;width:628px;font-size:14px;line-height:24px;color:var(--body-text)}
.btn.welcome-signin{left:328px;top:211px;background:var(--button-grey);color:var(--white)}

.site-footer{position:absolute;left:0;top:1118px;width:1200px;height:82px;
  background:linear-gradient(var(--footer-top),var(--footer-bottom))}
.footer-nav{position:absolute;left:107px;top:20px;display:flex;font-family:"Open Sans",sans-serif;font-size:11px;color:var(--ink);letter-spacing:.1px}
.footer-nav span{padding:0 15px}
.footer-nav span:first-child{padding-left:0}
.footer-nav span+span{border-left:1px solid var(--ink)}
</style>
</head>
<body>
<header class="site-header">
  <div class="brand">Recruitment site</div>
  <nav class="main-nav">
    <span>Home</span><span>About Us</span><span>Login</span><span>Services</span><span>Current Openings</span><span>Contact Us</span>
  </nav>
</header>

<div class="hero-backdrop" role="img" aria-label="Black and white photograph of an oil refinery at dusk with towers and chimneys"></div>

<p class="hero-intro">Some useful information, comments regarding our company, services etc sot hat user will get some interest to register on this ite or login this site. Any information etc..</p>

<section class="login-card">
  <div class="field user">Username or email here</div>
  <div class="field pass">Enter password</div>
  <div class="btn signin">Sign in</div>
  <p class="login-note forgot">Forgot password <a>click here</a></p>
  <p class="login-note register">New User <a>Register here</a></p>
</section>

<section class="welcome-card">
  <div class="welcome-photo" role="img" aria-label="Photograph of a gas processing plant with yellow pipework under a blue sky"></div>
  <h1 class="welcome-title">Welcome to Oil and Gas company</h1>
  <p class="welcome-text">the lorem ipsum text will be here the lorem ipsum text will be here the lorem ipsum text will be here the lorem ipsum text will be here the lorem ipsum text will be here the lorem ipsum text will be here the lorem ipsum text will be here the lorem ipsum text will be here the lorem ipsum text will be here the lorem ipsum text will be here the lorem ipsum text will be here the lorem ipsum text will be here the lorem ipsum text will be here</p>
  <div class="btn welcome-signin">Sign in</div>
</section>

<footer class="site-footer">
  <nav class="footer-nav">
    <span>Home</span><span>About Us</span><span>Login</span><span>Services</span><span>Current Openings</span><span>Privacy policy</span><span>Terms and conditions</span><span>Sitemap</span><span>Contact Us</span>
  </nav>
</footer>
</body>
</html>
```